BrightKeel Business Card Contest

We are looking for a modern business card that catches attention and is unique. Attached is the brand guide and logo files. Please note that the back side (not the side with our name and info) with be UV raise printed, so have fun with the design there. We want to include Name, Title, Phone number, email, website.

Contact Information for Business Card

Please see project description

```html
<!DOCTYPE html>
<html lang="en">
<head>
<meta charset="utf-8">
<title>BrightKeel Business Card</title>
<link rel="stylesheet" href="https://fonts.googleapis.com/css2?family=Poppins:wght@400;600&display=swap">
<style>
  :root {
    --stage-light: #5c5c5c;
    --stage-dark: #2a2a2a;
    --card-white: #ffffff;
    --card-black: #16181c;
    --pattern-dark: #23262c;
    --ink: #16181f;
    --navy: #1d3f9a;
    --blue: #1e7fe0;
    --sky: #27c1f0;
    --steel: #a9bed3;
    --orange: #ff7a12;
    --red: #e5231b;
  }
  * { box-sizing: border-box; margin: 0; padding: 0; }
  html, body { width: 1200px; height: 781px; overflow: hidden; }
  body {
    background: radial-gradient(ellipse at 50% 40%, var(--stage-light), var(--stage-dark) 80%);
    font-family: "Poppins", sans-serif;
    position: relative;
  }
  .card {
    position: absolute;
    top: 247px;
    width: 500px;
    height: 286px;
    border-radius: 3px;
    box-shadow: 0 18px 40px rgba(0,0,0,.45);
    overflow: hidden;
  }
  .card--back { left: 70px; background: var(--card-black); }
  .card--front { left: 630px; background: var(--card-white); }

  .uv-pattern {
    position: absolute; inset: 0;
    background: linear-gradient(135deg, var(--pattern-dark), var(--card-black) 60%, var(--pattern-dark));
  }
  .back-wordmark {
    position: absolute; inset: 0;
    display: flex; align-items: center; justify-content: center; gap: 10px;
    color: var(--card-white);
    font-weight: 600; font-size: 26px; letter-spacing: .5px;
  }
  .back-wordmark .mark-square { width: 16px; height: 16px; background: var(--sky); }

  .front-wordmark {
    position: absolute; left: 40px; top: 112px;
    font-weight: 600; font-size: 34px; color: var(--ink); letter-spacing: -.5px;
  }
  .divider { position: absolute; left: 262px; top: 78px; }
  .contact { position: absolute; left: 288px; top: 82px; color: var(--ink); }
  .contact__name { font-weight: 600; font-size: 22px; line-height: 1.1; }
  .contact__title { font-size: 11px; margin-top: 2px; }
  .contact__rule { width: 46px; height: 2px; background: var(--ink); margin: 6px 0 10px; }
  .contact__line { display: flex; align-items: center; gap: 7px; font-size: 11.5px; line-height: 1.7; }
  .contact__line svg { width: 10px; height: 10px; fill: var(--ink); flex: none; }

  .color-band { position: absolute; left: 0; right: 0; bottom: 0; height: 10px; display: flex; }
  .color-band span { flex: 1; }
  .band-navy { background: var(--navy); }
  .band-blue { background: var(--blue); }
  .band-sky { background: var(--sky); }
  .band-steel { background: var(--steel); }
  .band-orange { background: var(--orange); flex: .6 !important; }
  .band-red { background: var(--red); flex: .6 !important; }
</style>
</head>
<body>
  <section class="card card--back">
    <div class="uv-pattern" role="img" aria-label="UV raised repeating pattern of brand marks"></div>
    <div class="back-wordmark"><span class="mark-square"></span>BrightKeel</div>
  </section>

  <section class="card card--front">
    <div class="front-wordmark">BrightKeel</div>
    <svg class="divider" width="4" height="120" viewBox="0 0 4 120">
      <defs>
        <linearGradient id="divider-grad" x1="0" y1="1" x2="0" y2="0">
          <stop offset="0" stop-color="#1d3f9a"/>
          <stop offset=".5" stop-color="#27c1f0"/>
          <stop offset=".8" stop-color="#ff7a12"/>
          <stop offset="1" stop-color="#e5231b"/>
        </linearGradient>
      </defs>
      <rect x="1" y="0" width="2" height="120" fill="url(#divider-grad)"/>
    </svg>
    <div class="contact">
      <div class="contact__name">Dana Ellery</div>
      <div class="contact__title">Director</div>
      <div class="contact__rule"></div>
      <div class="contact__line">
        <svg viewBox="0 0 10 10"><path d="M2 0l2 2.5-1 1.2c.7 1.3 1.6 2.2 2.8 2.8L7 5.5 10 7.5 9 10C4 9.6.4 6 0 1z"/></svg>
        555-014-2290
      </div>
      <div class="contact__line">
        <svg viewBox="0 0 10 10"><path d="M0 2h10v6H0zM0 2l5 3.5L10 2" stroke="#fff" stroke-width=".8"/></svg>
        de@brightkeel.com
      </div>
      <div class="contact__line">
        <svg viewBox="0 0 10 10"><circle cx="5" cy="5" r="4.5"/><path d="M.5 5h9M5 .5c-2.5 3-2.5 6 0 9M5 .5c2.5 3 2.5 6 0 9" stroke="#fff" stroke-width=".7" fill="none"/></svg>
        brightkeel.com
      </div>
    </div>
    <div class="color-band">
      <span class="band-navy"></span><span class="band-blue"></span><span class="band-sky"></span>
      <span class="band-steel"></span><span class="band-orange"></span><span class="band-red"></span>
    </div>
  </section>
</body>
</html>
```